Brickline Rentals podcast postcard

I've launched a podcast about apartment investing, ownership and management which is newly up on orbix and wavlino. I want to create a postcard that I can mail to my client base to get them to subscribe

```html
<!DOCTYPE html>
<html lang="en">
<head>
<meta charset="UTF-8">
<title>Brickline Rentals – Podcast Postcard</title>
<link href="https://fonts.googleapis.com/css2?family=Oswald:wght@700&family=Montserrat:wght@400;500;600&display=swap" rel="stylesheet">
<style>
  :root {
    --navy: #14285a;
    --blue: #1f67b1;
    --white: #ffffff;
    --paper: #fbfbfb;
    --stamp: #e3e3e3;
    --ink: #111111;
    --backdrop: #a4a4a4;
  }
  * { box-sizing: border-box; margin: 0; padding: 0; }
  html, body { width: 1200px; height: 1200px; overflow: hidden; }
  body {
    background: var(--backdrop);
    font-family: "Montserrat", sans-serif;
    display: flex;
    flex-direction: column;
    align-items: center;
    justify-content: center;
    gap: 40px;
  }
  .postcard {
    position: relative;
    width: 780px;
    height: 520px;
    background: var(--paper);
    overflow: hidden;
    box-shadow: 0 6px 18px rgba(0,0,0,0.25);
  }

  /* ---------- Shared ---------- */
  .contact-list { display: flex; flex-direction: column; gap: 8px; white-space: nowrap; }
  .contact-item { display: flex; align-items: center; gap: 12px; }
  .contact-item.phone { font-size: 22px; font-weight: 500; letter-spacing: 3px; }
  .contact-item.web { font-size: 16px; letter-spacing: 2px; }
  .contact-icon { width: 20px; height: 20px; flex: none; }
  .cta-label {
    font-family: "Oswald", sans-serif;
    font-weight: 700;
    font-size: 26px;
    line-height: 1;
    letter-spacing: 1px;
    white-space: nowrap;
  }
  .platforms { display: flex; align-items: center; gap: 16px; white-space: nowrap; }
  .platform {
    display: flex; align-items: center; gap: 6px;
    font-size: 17px; font-weight: 600; color: var(--white);
  }
  .platform-dot { width: 12px; height: 12px; border-radius: 50%; background: var(--white); }

  /* ---------- Front ---------- */
  .front-header { position: absolute; left: 48px; top: 26px; z-index: 2; }
  .brand-title {
    font-family: "Oswald", sans-serif;
    font-weight: 700;
    font-size: 46px;
    line-height: 1;
    letter-spacing: 1px;
    color: var(--navy);
    text-transform: uppercase;
  }
  .tagline-band {
    display: inline-block;
    margin-top: 6px;
    margin-left: -14px;
    background: var(--blue);
    color: var(--white);
    font-size: 17px;
    letter-spacing: 3px;
    padding: 4px 16px 5px;
    text-transform: uppercase;
    white-space: nowrap;
  }
  .tagline-band strong { font-weight: 600; }
  .front-photo {
    position: absolute;
    left: 0; right: 0;
    top: 116px;
    height: 290px;
    background:
      linear-gradient(180deg, rgba(251,251,251,1) 0%, rgba(251,251,251,0) 18%),
      linear-gradient(180deg, #d9b6c6 0%, #f0c7a6 28%, #3f5f86 45%, #8a8f95 62%, #7c7d7e 78%, #6fb7b0 100%);
  }
  .info-band {
    position: absolute;
    left: 0; right: 0; bottom: 0;
    height: 130px;
    background: linear-gradient(180deg, var(--blue) 0%, var(--navy) 100%);
    color: var(--white);
    display: flex;
    align-items: center;
    padding: 0 36px 0 44px;
  }
  .divider { width: 3px; height: 64px; background: var(--white); margin: 0 28px; flex: none; }
  .listen-cta { display: flex; align-items: center; gap: 20px; }

  /* ---------- Back ---------- */
  .back-photo {
    position: absolute;
    left: 0; top: 0;
    width: 400px; height: 400px;
    background: radial-gradient(circle at 55% 35%, #3a4d78 0%, #1c2a52 55%, #121c3c 100%);
  }
  .back-cta {
    position: absolute;
    left: 196px; top: 292px;
    color: var(--white);
    display: flex; flex-direction: column; gap: 12px;
  }
  .back-band {
    position: absolute;
    left: 0; bottom: 0;
    width: 400px; height: 120px;
    background: linear-gradient(180deg, var(--blue) 0%, var(--navy) 100%);
    color: var(--white);
    display: flex; align-items: center;
    padding-left: 36px;
  }
  .address-side {
    position: absolute;
    left: 400px; top: 0; right: 0; bottom: 0;
    background: var(--paper);
  }
  .stamp-box {
    position: absolute;
    right: 36px; top: 40px;
    width: 92px; height: 72px;
    background: var(--stamp);
  }
  .address-lines {
    position: absolute;
    left: 50px; right: 40px; top: 220px;
    display: flex; flex-direction: column; gap: 44px;
  }
  .address-line { height: 2px; background: var(--ink); }
</style>
</head>
<body>

  <!-- Front of postcard -->
  <section class="postcard postcard-front">
    <div class="front-photo" role="img" aria-label="Photo of a modern white apartment building with a wooden deck and pool at sunset"></div>
    <header class="front-header">
      <h1 class="brand-title">Brickline Rentals</h1>
      <div class="tagline-band"><strong>Podcast:</strong> Investing | Owning | Managing</div>
    </header>
    <div class="info-band">
      <div class="contact-list">
        <div class="contact-item phone">
          <svg class="contact-icon" viewBox="0 0 20 20" aria-hidden="true">
            <circle cx="10" cy="10" r="9" fill="none" stroke="#fff" stroke-width="1.6"/>
            <path d="M7 5.5c-.8.4-1.4 1.3-1 2.6.7 2.4 2.6 4.6 5 5.7 1.2.5 2.2 0 2.7-.8l-1.6-1.5-1.1.6c-1-.5-2-1.6-2.5-2.6l.7-1z" fill="#fff"/>
          </svg>
          <span>555 014 2290</span>
        </div>
        <div class="contact-item web">
          <svg class="contact-icon" viewBox="0 0 20 20" aria-hidden="true">
            <g fill="none" stroke="#fff" stroke-width="1.4">
              <circle cx="10" cy="10" r="8.5"/>
              <ellipse cx="10" cy="10" rx="4" ry="8.5"/>
              <path d="M1.5 10h17M3 5.5h14M3 14.5h14"/>
            </g>
          </svg>
          <span>www.bricklinerentals.net</span>
        </div>
      </div>
      <div class="divider"></div>
      <div class="listen-cta">
        <span class="cta-label">SUBSCRIBE ON</span>
        <div class="platforms">
          <span class="platform"><span class="platform-dot"></span>orbix</span>
          <span class="platform"><span class="platform-dot"></span>wavlino</span>
        </div>
      </div>
    </div>
  </section>

  <!-- Back of postcard -->
  <section class="postcard postcard-back">
    <div class="back-photo" role="img" aria-label="Photo of hands in a navy suit holding a small model house with a set of keys"></div>
    <div class="back-cta">
      <span class="cta-label">SUBSCRIBE ON</span>
      <div class="platforms">
        <span class="platform"><span class="platform-dot"></span>orbix</span>
        <span class="platform"><span class="platform-dot"></span>wavlino</span>
      </div>
    </div>
    <div class="back-band">
      <div class="contact-list">
        <div class="contact-item phone">
          <svg class="contact-icon" viewBox="0 0 20 20" aria-hidden="true">
            <circle cx="10" cy="10" r="9" fill="none" stroke="#fff" stroke-width="1.6"/>
            <path d="M7 5.5c-.8.4-1.4 1.3-1 2.6.7 2.4 2.6 4.6 5 5.7 1.2.5 2.2 0 2.7-.8l-1.6-1.5-1.1.6c-1-.5-2-1.6-2.5-2.6l.7-1z" fill="#fff"/>
          </svg>
          <span>555 014 2290</span>
        </div>
        <div class="contact-item web">
          <svg class="contact-icon" viewBox="0 0 20 20" aria-hidden="true">
            <g fill="none" stroke="#fff" stroke-width="1.4">
              <circle cx="10" cy="10" r="8.5"/>
              <ellipse cx="10" cy="10" rx="4" ry="8.5"/>
              <path d="M1.5 10h17M3 5.5h14M3 14.5h14"/>
            </g>
          </svg>
          <span>www.bricklinerentals.net</span>
        </div>
      </div>
    </div>
    <div class="address-side">
      <div class="stamp-box"></div>
      <div class="address-lines">
        <div class="address-line"></div>
        <div class="address-line"></div>
        <div class="address-line"></div>
      </div>
    </div>
  </section>

</body>
</html>
```